Flyer Design - High Quality

*** Although this current job contest is listed as a ‘one-off contest’ we are also looking at working with a graphic designer long-term, which will include quite regular design work. So even though this is just a small job, if you want to & you do a good job on this, we would love to look at working with you on a regular basis.
* The winning designer will also get a freelance job designing another flyer in same design
Job Basics:
1. the design of a ….
Promotional corporate flyer - size = A4 - approx 6 or 7 pages.
*** The design will need to be extremely high quality/professional. Must be of a similar or better standard as the attached flyers – 1) Dell Warrick_Info Pack & 2) DrOwen Pellby
* Please view these flyers first to ensure you can create a flyer of similar or better quality before proceeding.
Specific Requirements:
1. high-quality, professional promotional flyer [size = A4 - for online use predominantly . I.e. not for printing necessarily] using the text, images and basic instructions outlined on the word document attached - 'Flyer_All talks in 1_guidelines'.
2. Examples of similar quality (good) designs = 1) Dell Warrick_Info Pack & 2) DrOwen Pellby
Background:
I am a motivational speaker on health, well-being and work-life balance. This flyer is to be used for promotional purposes when clients inquire about me speaking at their conference. Dell Warrick & Owen Pellby are speakers who do somewhat similar talks to me, and who have flyers that I really like.
Theme: My general theme is ‘health and well-being’ (we're a little bit more towards natural health and Eastern medicine, but don't want it too ‘eastern’ if you know what I mean).
Main Look & Feel … to be conveyed:
Professional / Corporate
Health, Vitality and happiness (fresh, modern and vital)
eye-catching / attention grabbing
* The design should represent a balance between highly sophisticated, professional and classy - corporate savvy - with a hint of 'natural health, Eastern wisdom and a general ‘high energy/fresh health and vitality feel'. While we would like the design to convey some aspect of ‘ natural/Eastern’ wisdom), we predominantly want to convey the idea of ‘modern’ health (i.e. fresh, modern and vital).
Colours:
We are open to your creative suggestions, but were generally thinking something along the lines of the colours in our corporate logo –
dark blue, aqua blue, grey – see logo (QEV_300kb.jpg) in attachments
- possibly with some bright green, orange etc if you think it might suit – to help give it the ‘natural health’ feel.
* Notes:
1. SAVING YOUR TIME: If you just want to start just doing a quickish design of the first 1-2 pages and submitting that (images for these pages attached - though use own images if you think they are better), then that’s fine. Then we can let you know if it is along the lines of something we like or not. This way, you can do something relatively quickly, without wasting too much time, if it is definitely not something we like. Hope that helps - we are always conscious of trying to make things good for you as a designer too.
2. Do not feel completely bound to the ideas suggested/asked for. Feel free to convey the basic ideas/keys but feel free to use/follow some of your own ideas/creative desires.
3. Any photos/images should be royalty free (or ask us if we want to pay for it) and not widely used or seen in the public domain - i.e. we don’t want people to have seen the photo/image elsewhere (within reason).
Thanks a lot and look forward to receiving your first design!
Cheers
Tobin
Predominantly corporates / business groups.
Graphic Designer

```html
<!DOCTYPE html>
<html lang="en">
<head>
<meta charset="utf-8">
<title>Sessions Include – Yoga &amp; Meditation Workshops</title>
<link rel="stylesheet" href="https://fonts.googleapis.com/css2?family=Tinos&family=Roboto+Condensed:wght@300;400;700&display=swap">
<style>
  :root {
    --navy: #0f4f86;
    --navy-deep: #0b3f70;
    --aqua: #29b6e6;
    --aqua-light: #5fd0f2;
    --gold: #c8b36d;
    --grey-band: #cfcfcf;
    --text-grey: #8a8a8a;
    --text-dark: #555555;
    --heading-blue: #1a5a9a;
    --key-green: #39b54a;
    --key-red: #e8224a;
    --key-orange: #f58a1f;
    --white: #ffffff;
  }
  * { margin: 0; padding: 0; box-sizing: border-box; }
  html, body { width: 848px; height: 1200px; overflow: hidden; background: var(--white); }
  .page { position: relative; width: 848px; height: 1200px; font-family: "Roboto Condensed", "Arial Narrow", sans-serif; }

  .masthead {
    position: absolute; top: 0; left: 0; width: 848px; height: 156px;
    background: linear-gradient(180deg, var(--navy) 0%, var(--navy-deep) 100%);
    text-align: center; color: var(--white);
  }
  .masthead-title { font-family: "Tinos", "Times New Roman", serif; font-weight: 400; font-size: 54px; line-height: 1; padding-top: 20px; }
  .masthead-rule { width: 640px; height: 1px; margin: 14px auto 0; background: linear-gradient(90deg, transparent, rgba(255,255,255,.55), transparent); }
  .legend { display: flex; justify-content: center; align-items: center; gap: 26px; margin-top: 14px; font-size: 18px; font-weight: 300; color: var(--aqua-light); }
  .legend-item { display: flex; align-items: center; gap: 8px; }
  .key { display: inline-flex; align-items: center; justify-content: center; height: 22px; min-width: 22px; padding: 0 4px; font-size: 14px; font-weight: 700; color: var(--white); }
  .key-k { background: var(--key-green); }
  .key-wb { background: var(--key-red); }
  .key-hd { background: var(--key-orange); }

  .hero-photo {
    position: absolute; top: 156px; left: 0; width: 848px; height: 424px;
    background: linear-gradient(100deg, #6b4a34 0%, #8a6448 35%, #a47c5c 55%, #4a8fc4 72%, #9fc6e6 100%);
  }
  .grey-band { position: absolute; top: 580px; left: 0; width: 848px; height: 19px; background: var(--grey-band); }

  .session-band { position: absolute; top: 599px; left: 0; width: 848px; height: 94px; background: var(--gold); color: var(--white); padding: 20px 0 0 26px; }
  .session-title { font-family: "Tinos", "Times New Roman", serif; font-weight: 400; font-size: 40px; line-height: 1; display: flex; align-items: center; gap: 10px; }
  .session-title .key { height: 24px; font-size: 13px; }
  .session-tagline { margin-top: 12px; font-size: 13px; font-weight: 300; }

  .session-intro { position: absolute; top: 724px; left: 26px; width: 796px; font-size: 15px; font-weight: 300; line-height: 26px; color: var(--text-grey); text-align: justify; letter-spacing: .3px; }

  .includes-heading { position: absolute; top: 858px; left: 26px; display: flex; align-items: center; gap: 14px; font-size: 34px; font-weight: 700; color: var(--heading-blue); }
  .includes-list { position: absolute; top: 922px; left: 26px; width: 790px; list-style: none; font-size: 20px; font-weight: 300; color: var(--text-dark); line-height: 30px; }
  .includes-list li { position: relative; padding-left: 36px; margin-bottom: 26px; }
  .includes-list li::before { content: ""; position: absolute; left: 2px; top: 10px; width: 11px; height: 11px; background: var(--text-dark); }

  .footer-band { position: absolute; top: 1168px; left: 0; width: 848px; height: 32px; background: var(--aqua); }
  .testimonial { position: absolute; top: 1182px; left: 0; width: 848px; text-align: center; font-size: 9px; font-weight: 400; color: var(--navy-deep); }
  .lotus-mark { position: absolute; top: 1118px; left: 728px; width: 90px; height: 60px; border-radius: 45px 45px 0 0; background: linear-gradient(180deg, var(--aqua-light), var(--aqua)); }
</style>
</head>
<body>
<div class="page">
  <header class="masthead">
    <h1 class="masthead-title">Sessions Include</h1>
    <div class="masthead-rule"></div>
    <div class="legend">
      <span class="legend-item"><span class="key key-k">K</span>= available as a keynote (40 – 90min)</span>
      <span class="legend-item"><span class="key key-wb">WB</span>= workshop or breakout</span>
      <span class="legend-item"><span class="key key-hd">HD</span>= half day session</span>
    </div>
  </header>

  <div class="hero-photo" role="img" aria-label="Photo of a woman meditating cross-legged inside a rock cave beside the ocean under a blue sky"></div>
  <div class="grey-band"></div>

  <section class="session-band">
    <h2 class="session-title">Yoga &amp; Meditation Workshops <span class="key key-wb">WB</span></h2>
    <p class="session-tagline">re-energise, re-charge &amp; re-enliven peak mind-body performance</p>
  </section>

  <p class="session-intro">Combining best of East &amp; West principles with fascinating insights from the popular new fields of natural health and ‘mind-body’ medicine, these sessions show people hands-on exercises and practical activities for de-stressing and re-charging.</p>

  <h3 class="includes-heading">
    <svg width="16" height="24" viewBox="0 0 16 24" aria-hidden="true"><path d="M0 0 L16 12 L0 24 Z" fill="var(--heading-blue)"/></svg>
    Includes :
  </h3>
  <ul class="includes-list">
    <li>Breathing &amp; Meditation practices to reduce tension and calm the mind</li>
    <li>Yoga Postures – a simple ‘do-it-yourself’ yoga routine that can be done anywhere, anytime suitable for home or office (normal work clothing is fine).</li>
    <li>Office stretching &amp; workplace health techniques</li>
  </ul>

  <div class="footer-band"></div>
  <div class="lotus-mark" role="img" aria-label="Decorative lotus flower ornament"></div>
  <p class="testimonial">“Awesome” - Lena Varro - Kestrel Group</p>
</div>
</body>
</html>
```